Business Card Design

I need a Business Card that will catch the attention that will not get thrown in a Drawer. I have 23 companies I use for Auto, Home, Life, and Business Insurance. I make sure that people have the best coverage for the $ spent.

Industry/Entity Type

Business

Contact Information for Business Card

Torvin Insurance Agency, Inc., Derek Halloway, 4735 West Fallow Lane Corridan Falls, Elmshire 52913 555-287-6194, www.torvinagency-example.com, Facebook, LinkedIn, Google+

```html
<!DOCTYPE html>
<html lang="en">
<head>
<meta charset="utf-8">
<title>Torvin Insurance Agency – Business Card</title>
<link rel="stylesheet" href="https://fonts.googleapis.com/css2?family=Arimo:wght@400;700&family=Open+Sans:wght@400;600&display=swap">
<style>
  :root {
    --page-bg: #d9d9d9;
    --card-white: #f6f6f6;
    --card-black: #0b0b0b;
    --accent-orange: #eaa43a;
    --rule-orange: #e39a2a;
    --text-light: #f1f1f1;
    --text-muted: #cfcfcf;
  }
  * { box-sizing: border-box; margin: 0; padding: 0; }
  html, body { width: 1200px; height: 750px; overflow: hidden; }
  body {
    background: radial-gradient(ellipse at 60% 35%, #ececec 0%, var(--page-bg) 75%);
    position: relative;
  }
  .business-card {
    position: absolute;
    left: 75px; top: 75px;
    width: 1050px; height: 600px;
    border-radius: 34px;
    overflow: hidden;
    background: var(--card-black);
    box-shadow: 0 14px 30px rgba(0,0,0,.18);
  }
  .top-band {
    position: absolute; left: 0; top: 0; width: 100%; height: 130px;
    background: linear-gradient(180deg, #ffffff 0%, var(--card-white) 100%);
  }
  .company-name {
    position: absolute; left: 58px; bottom: 14px;
    font-family: "Arimo", Arial, sans-serif; font-weight: 700;
    font-size: 38px; color: var(--accent-orange);
    letter-spacing: .2px;
  }
  .top-rule {
    position: absolute; left: 0; top: 130px; width: 100%; height: 7px;
    background: var(--rule-orange);
  }
  .black-panel {
    position: absolute; left: 0; top: 137px; width: 100%; height: 293px;
    background: linear-gradient(160deg, #1a1a1a 0%, var(--card-black) 55%);
  }
  .bottom-rule {
    position: absolute; left: 0; top: 432px; width: 100%; height: 7px;
    background: #ffffff;
  }
  .bottom-gap {
    position: absolute; left: 0; top: 439px; width: 100%; height: 9px;
    background: var(--card-black);
  }
  .bottom-band {
    position: absolute; left: 0; top: 448px; width: 100%; height: 152px;
    background: linear-gradient(180deg, var(--accent-orange) 0%, #df9627 100%);
  }
  .person-name {
    position: absolute; left: 66px; top: 325px;
    font-family: "Arimo", Arial, sans-serif; font-weight: 400;
    font-size: 38px; color: var(--text-muted);
  }
  .person-name .initial { color: #ffffff; font-weight: 700; font-size: 44px; }
  .divider {
    position: absolute; left: 400px; top: 160px; width: 3px; height: 240px;
    background: linear-gradient(180deg, rgba(255,255,255,0) 0%, rgba(255,255,255,.75) 45%, rgba(255,255,255,0) 100%);
  }
  .contact-list {
    position: absolute; left: 440px; top: 165px;
    list-style: none;
    font-family: "Open Sans", Arial, sans-serif; font-size: 25px;
    color: var(--text-light); line-height: 1.3;
  }
  .contact-item { display: flex; align-items: flex-start; margin-bottom: 22px; }
  .contact-icon { width: 34px; height: 34px; flex: none; margin-right: 26px; margin-top: 1px; }
  .contact-item.address .contact-icon { margin-top: 48px; }
</style>
</head>
<body>
  <div class="business-card">
    <div class="top-band">
      <div class="company-name">Torvin Insurance Agency</div>
    </div>
    <div class="top-rule"></div>
    <div class="black-panel"></div>
    <div class="bottom-rule"></div>
    <div class="bottom-gap"></div>
    <div class="bottom-band"></div>

    <div class="person-name"><span class="initial">D</span>erek <span class="initial">H</span>alloway</div>
    <div class="divider"></div>

    <ul class="contact-list">
      <li class="contact-item phone">
        <svg class="contact-icon" viewBox="0 0 34 34" aria-hidden="true">
          <circle cx="17" cy="17" r="16" fill="#f1f1f1"/>
          <path d="M11 9c1-1 2-1 3 0l2 3c.5 1 0 2-1 2.5 1 2.5 2.5 4 5 5 .5-1 1.5-1.5 2.5-1l3 2c1 1 1 2 0 3-2 2-5 2-9-2s-5-8-5.5-12.5z" fill="#111"/>
        </svg>
        <span>555-287-6194</span>
      </li>
      <li class="contact-item web">
        <svg class="contact-icon" viewBox="0 0 34 34" aria-hidden="true">
          <circle cx="17" cy="17" r="16" fill="#f1f1f1"/>
          <g fill="none" stroke="#111" stroke-width="1.8">
            <circle cx="17" cy="17" r="9"/>
            <ellipse cx="17" cy="17" rx="4" ry="9"/>
            <path d="M8 17h18M9.5 12.5h15M9.5 21.5h15"/>
          </g>
        </svg>
        <span>www.torvinagency-example.com</span>
      </li>
      <li class="contact-item address">
        <svg class="contact-icon" viewBox="0 0 34 34" aria-hidden="true">
          <circle cx="17" cy="17" r="16" fill="#f1f1f1"/>
          <path d="M17 7a7 7 0 0 0-7 7c0 5 7 13 7 13s7-8 7-13a7 7 0 0 0-7-7z" fill="#111"/>
          <circle cx="17" cy="14" r="2.6" fill="#f1f1f1"/>
        </svg>
        <span>4735 West Fallow Lane Corridan Falls<br>Elmshire 52913</span>
      </li>
    </ul>
  </div>
</body>
</html>
```